Verpackung für Hanf-Nudeln gesucht
Zielgruppe
Wir haben Hanf & Natur Shops und Onlineshop. Zielgruppe sind Menschen die gesund und bewusst Leben möchten.
Aufgabenstellung
Verpackung für Hanf-Nudeln (Suppen-, Band-, Spaghetti-, Hörnchennudeln). 500g abgepackt.
Wichtig: handgemacht in Österreich, 100 % vegan und bio
sie enthalten Dinkel- und Hanfmehl sowie geringe Mengen an Kelmer FELSENSALZ und werden mit nitratfreiem Wasser erzeugt. Die Hanfnudeln sind vollkommen frei von synthetischen Hilfsmitteln. Kochzeit ca. 3 Minuten., Info für alle Allergiker, Hanfnudeln sind NICHT GLUTENFREI., Zutaten: Dinkel, Hanfmehl, Steinsalz, nitratfreies Wasser
Verpackungsvorschläge bitte
Modernes Design, passend zu unseren anderen Velmoranda Produkten

```html
<!DOCTYPE html>
<html lang="de">
<head>
<meta charset="utf-8">
<title>Velmoranda Hanf-Pasta – Hörnchennudeln</title>
<link rel="stylesheet" href="https://fonts.googleapis.com/css2?family=Abril+Fatface&family=Montserrat:wght@300;400;700&display=swap">
<style>
  :root {
    --backdrop: #ececec;
    --kraft: #c8a47c;
    --kraft-shade: #bf9a71;
    --kraft-fold: #a98660;
    --label: #e4e4e4;
    --ink: #1f1f1f;
    --paper-white: #ffffff;
    --brand-green: #4f8a4f;
    --pasta-light: #f4e6bd;
    --pasta-deep: #ecc970;
  }
  html, body {
    margin: 0;
    width: 1200px;
    height: 1200px;
    overflow: hidden;
    background: var(--backdrop);
  }
  .package {
    position: absolute;
    left: 365px;
    top: 105px;
    width: 470px;
    height: 990px;
    display: block;
  }
  .brand-name { font-family: "Montserrat", sans-serif; font-weight: 700; font-size: 22px; fill: var(--ink); }
  .hero-word { font-family: "Abril Fatface", serif; font-size: 300px; fill: var(--paper-white); }
  .variety { font-family: "Montserrat", sans-serif; font-weight: 300; font-size: 31px; fill: var(--paper-white); letter-spacing: 1px; }
  .claim { font-family: "Montserrat", sans-serif; font-weight: 400; font-size: 15px; fill: var(--ink); }
  .dotted { fill: none; stroke: var(--ink); stroke-width: 2.4; stroke-dasharray: 0.1 7; stroke-linecap: round; }
  .icon-line { fill: none; stroke: var(--ink); stroke-width: 2; stroke-linejoin: round; stroke-linecap: round; }
</style>
</head>
<body>
<svg class="package" viewBox="0 0 660 1390" xmlns="http://www.w3.org/2000/svg" aria-label="Velmoranda Hanf-Pasta Hörnchennudeln, 500 g">
  <defs>
    <linearGradient id="pasta-fill" x1="0" y1="0" x2="0" y2="1">
      <stop offset="0" stop-color="var(--pasta-deep)"/>
      <stop offset="1" stop-color="var(--pasta-light)"/>
    </linearGradient>
  </defs>

  <!-- bag body -->
  <rect class="bag" x="0" y="0" width="660" height="1390" fill="var(--kraft)"/>
  <line class="bag-fold" x1="0" y1="108" x2="660" y2="108" stroke="var(--kraft-fold)" stroke-width="2"/>

  <!-- decorative pasta line illustration area -->
  <g role="img" aria-label="Linienillustration fliegender Pasta-Schleifen">
    <rect x="325" y="75" width="335" height="1030" fill="var(--kraft-shade)" opacity="0.55"/>
  </g>

  <!-- top seal label -->
  <rect class="seal-label" x="238" y="0" width="177" height="280" fill="var(--label)"/>
  <circle cx="326.5" cy="165" r="26" fill="var(--brand-green)"/>
  <text class="brand-name" x="326.5" y="246" text-anchor="middle">Velmoranda</text>

  <!-- product window -->
  <g role="img" aria-label="Sichtfenster mit Fusilli-Nudeln">
    <rect x="100" y="760" width="450" height="355" rx="14" fill="url(#pasta-fill)"/>
  </g>

  <!-- headline with swoosh -->
  <text class="hero-word" x="0" y="600" textLength="660" lengthAdjust="spacingAndGlyphs">Pasta</text>
  <path class="swoosh" d="M0 705 C 140 690 330 620 560 500 C 330 650 150 760 0 800 Z" fill="var(--paper-white)"/>

  <text class="variety" x="530" y="710" text-anchor="end">HÖRNCHEN-</text>
  <text class="variety" x="530" y="745" text-anchor="end">NUDELN</text>

  <!-- claims box -->
  <rect class="dotted" x="108" y="1153" width="430" height="165"/>
  <line class="dotted" x1="270" y1="1153" x2="270" y2="1318"/>
  <line class="dotted" x1="270" y1="1235" x2="538" y2="1235"/>

  <g role="img" aria-label="Symbol: Hände halten ein Herz in den Farben Österreichs">
    <rect x="155" y="1175" width="56" height="50" rx="6" fill="var(--kraft-shade)"/>
  </g>
  <text class="claim" x="183" y="1278" text-anchor="middle">handgemacht</text>
  <text class="claim" x="183" y="1298" text-anchor="middle">in Österreich</text>

  <path class="icon-line" d="M334 1182 L350 1214 L366 1182 M340 1182 L350 1203 L360 1182"/>
  <text class="claim" x="400" y="1203">100 % vegan</text>

  <path class="icon-line" d="M336 1290 C 332 1268 348 1254 368 1252 C 368 1274 356 1290 336 1290 Z M336 1290 L356 1266"/>
  <text class="claim" x="400" y="1279">100 % bio</text>
</svg>
</body>
</html>
```